Brontaro Web Site

Redesigned web site for Brontaro Ltd (www.brontaro-example.co.uk). This is to feature new logo (attached). Brontaro Ltd is a company which specialises in Geographic Information Systems and Geographic data - we call ourselves GIS Data Specialists. We are looking for something which conveys our professionalism and our experience. There will be more pages than on the current Brontaro website. There will be: Home, Data Migration, Data Cleansing & Validation, Data Analysis, Data Maintenance, Data Quality and an About Us page. All these should be accessible from each page on the website.
Updates
I didn't really think to say that the content of the web site is going to change from the current one we have. There will be more pages than on the current one. They will be: Home, Data Migration, Data Cleansing & Validation, Data Analysis, Data Maintenance, Data Quality and an About Us page. All these should be accessible from each page on the website. I didn't really think through the fact that the number of pages / areas to access can influence the layout of the site, sorry.
Target Market(s)
Utility Companies (e.g. telecommunications providers, energy companies), local government.
Industry/Entity Type
It Company
Look and feel

```html
<!DOCTYPE html>
<html lang="en">
<head>
<meta charset="utf-8">
<title>Brontaro – GIS Data Specialists</title>
<link href="https://fonts.googleapis.com/css2?family=Source+Sans+3:wght@400;600&display=swap" rel="stylesheet">
<style>
:root{
  --page:#ffffff;
  --haze-top:#d2d3d6;
  --haze-mid:#e6e7e9;
  --card:#ffffff;
  --header-top:#7199cb;
  --header-bottom:#34506f;
  --brand-grey:#8e949b;
  --accent:#86d2d4;
  --text:#8c8c8c;
  --heading:#7a7a7a;
  --link:#8f8f8f;
  --decor:#e3f1f2;
}
*{margin:0;padding:0;box-sizing:border-box}
html,body{width:1200px;height:1056px;overflow:hidden;background:var(--page)}
body{font-family:"Source Sans 3",Arial,sans-serif;color:var(--text)}
.stage{position:relative;width:1136px;height:1000px;transform:scale(1.0563);transform-origin:0 0}
.backdrop{position:absolute;left:0;top:0;width:930px;height:850px;
  background:linear-gradient(180deg,var(--haze-top) 0%,var(--haze-mid) 45%,#ffffff 100%);}
.backdrop::after{content:"";position:absolute;right:0;top:0;width:90px;height:100%;
  background:linear-gradient(90deg,rgba(255,255,255,0),#ffffff)}
.card{position:absolute;left:90px;top:28px;width:748px;height:822px;background:var(--card);
  border-radius:14px 14px 0 0;box-shadow:0 0 6px rgba(0,0,0,.18)}
.decor{position:absolute;left:90px;top:380px;width:210px;height:460px;
  background:radial-gradient(ellipse at 10% 55%,var(--decor) 0%,rgba(227,241,242,.5) 45%,rgba(255,255,255,0) 75%)}
.masthead{position:absolute;left:151px;top:0;width:267px;height:210px;
  background:linear-gradient(180deg,var(--header-top),var(--header-bottom))}
.brand{position:absolute;left:18px;top:110px;display:flex;align-items:center;gap:12px}
.brand-dot{width:22px;height:22px;border-radius:50%;background:var(--accent)}
.brand-name{font-size:38px;font-weight:600;color:var(--brand-grey);line-height:1}
.top-nav{position:absolute;top:197px;left:657px;display:flex;gap:17px;font-size:13px;color:#777}
.top-nav a{color:inherit;text-decoration:none}
.side{position:absolute;left:167px;top:247px}
.side h3{margin-left:11px;font-size:12.5px;font-weight:600;color:var(--heading);line-height:16px}
ul{list-style:none}
.side li,.services li{position:relative;padding-left:11px}
.side li{font-size:11.5px;line-height:14.5px}
.side li::before,.services li::before{content:"";position:absolute;left:0;width:5px;height:5px;border-radius:50%;background:var(--accent)}
.side li::before{top:5px}
a{color:var(--link)}
.main{position:absolute;left:371px;top:246px;width:387px}
.main h1{font-size:14px;font-weight:600;color:var(--heading);line-height:18px;margin-bottom:14px}
.main p{font-size:12px;line-height:15.5px;text-align:justify;margin-bottom:16px}
.main p strong{font-size:14px;font-weight:600;color:#6f6f6f}
.services{margin-top:8px}
.services li{font-size:12px;line-height:17px;padding-left:10px}
.services li::before{top:6px}
.terms{position:absolute;left:680px;top:731px;font-size:8px;color:#777}
.footer{position:absolute;left:314px;top:818px;font-size:12px;color:#8a8a8a}
</style>
</head>
<body>
<div class="stage">
  <div class="backdrop"></div>
  <div class="card"></div>
  <div class="decor" role="img" aria-label="Faint decorative brand motif"></div>

  <header class="masthead">
    <div class="brand"><span class="brand-dot"></span><span class="brand-name">Brontaro</span></div>
  </header>

  <nav class="top-nav"><a href="#">Home</a><a href="#">About Us</a></nav>

  <aside class="side">
    <h3>Products and Services</h3>
    <ul>
      <li><a href="#">Brontaro</a></li>
      <li><a href="#">Data Consultancy</a></li>
      <li><a href="#">Software Development</a></li>
      <li><a href="#">Software Products</a></li>
      <li><a href="#">Contact Us</a></li>
    </ul>
  </aside>

  <main class="main">
    <h1>Welcome to Brontaro</h1>
    <p>Brontaro was founded in 1994 by a group of geospatial software engineers that recognised the significant value that data, and the systems used to store and analyse this data, could bring to business.</p>
    <p><strong>Our Customers:</strong> We have worked with over 200 companies in a myriad of market sectors - from utilities, local and central government, oil and gas, to many spheres of the marine industry.</p>
    <p><strong>Our Pedigree:</strong> We provide a vast bank of knowledge and experience to offer an all encompassing service. This ensures that you, as a customer, reap the maximum benefits from your data and systems through utilising a combination of our skilled consultants, analysts and developers that will work with you and your requirements to help achieve your business objectives.</p>
    <p><strong>Our People:</strong> We have a wide ranging skill set including PROMETA 2 qualified Project Managers, fully qualified Software Developers and Experienced Data Consultants.</p>
    <p>We can be on hand to help with any or all parts of your data projects via:</p>
    <ul class="services">
      <li><a href="#">Data Consultancy</a></li>
      <li><a href="#">System Consultancy</a></li>
      <li><a href="#">Softwear Development</a></li>
      <li><a href="#">Data Migration</a></li>
      <li><a href="#">Data Cleansing &amp; Validation</a></li>
      <li><a href="#">Data Analysis</a></li>
      <li><a href="#">Data Maintenance</a></li>
      <li><a href="#">Data Quality</a></li>
    </ul>
  </main>

  <a class="terms" href="#">Terms and Conditions</a>
  <footer class="footer">© 2010 Brontaro Ltd. Registered in Scotland No. 204817</footer>
</div>
</body>
</html>
```